Criação de Papelaria Profissional para Construção & Engenharia
" Administração de obras: o cliente nos contrata para realizar a gestão da construção de sua casa (alto padrão), desde orçamentos, cronograma de obra, acompanhamento da obra e gestão da mão de obra. Desenvolvimento de novos negócios: Realizamos o estudo de viabilidade técnico-econômica de terrenos para realização de loteamentos, condomínios e empreendimentos verticais e prospectamos construtoras e loteadoras para apresentar o projeto. Gestão de Grupos de investimentos: Fracionamos investimentos do setor imobiliário em cotas para acelerar um determinado negócio. Ex: adquirimos um lote em condomínio, realizamos um projeto de casa alto padrão e calculamos o custo total entre terreno e obra. Fracionamos em contas de 50 mil e vendemos para arrecadar o valor total do investimento. Assim, construimos a casa e na hora da sua venda é dividido os lucros proporcionalmente as cotas adquiridas. "

```html
<!DOCTYPE html>
<html lang="pt-BR">
<head>
<meta charset="UTF-8">
<title>Envelope Saco – Vanta Engenharia</title>
<link rel="stylesheet" href="https://fonts.googleapis.com/css2?family=Montserrat:wght@500;600;700;800&display=swap">
<style>
  :root {
    --board: #d9d9d9;
    --panel: #e4e4e4;
    --navy: #15305a;
    --gold: #c7a467;
    --white: #ffffff;
  }
  * { margin: 0; padding: 0; box-sizing: border-box; }
  html, body { width: 1200px; height: 1200px; overflow: hidden; }
  body {
    background: var(--board);
    font-family: "Montserrat", sans-serif;
    position: relative;
  }
  .board-frame {
    position: absolute;
    left: 43px; top: 43px; width: 1114px; height: 1114px;
    background: var(--panel);
    border: 5px solid var(--navy);
  }
  .board-title {
    position: absolute;
    top: 22px; left: 50%;
    transform: translateX(-50%);
    background: var(--board);
    padding: 0 34px;
    color: var(--navy);
    font-weight: 800;
    font-size: 28px;
    letter-spacing: 1px;
    line-height: 44px;
    white-space: nowrap;
  }
  .envelope {
    position: absolute;
    top: 168px;
    width: 440px; height: 756px;
    background: var(--navy);
    overflow: hidden;
  }
  .envelope--front { left: 144px; }
  .envelope--back { left: 612px; }
  .envelope__stripe {
    position: absolute;
    left: 0; right: 0; bottom: 14px;
    height: 14px;
    background: var(--gold);
  }
  .envelope__flap { position: absolute; top: 0; left: 0; }
  .brand {
    position: absolute;
    left: 0; right: 0;
    display: flex; flex-direction: column; align-items: center;
    color: var(--white);
    font-weight: 600;
  }
  .brand__mark {
    width: 34px; height: 34px; border-radius: 50%;
    background: var(--gold);
    margin-bottom: 16px;
  }
  .brand__name { font-size: 74px; line-height: 1; letter-spacing: 2px; }
  .brand__sub { font-size: 18px; letter-spacing: 8px; margin-top: 8px; line-height: 1.2; }
  .envelope--front .brand { top: 355px; }
  .envelope--back .brand { top: 377px; }
  .envelope--back .brand__mark { width: 30px; height: 30px; }
  .envelope--back .brand__name { font-size: 60px; }
  .envelope--back .brand__sub { font-size: 15px; letter-spacing: 6px; }
  .contact-row {
    position: absolute;
    left: 24px; right: 16px; bottom: 46px;
    display: flex; justify-content: space-between; align-items: center;
    color: var(--white);
    font-size: 9px; font-weight: 500;
  }
  .contact-row__item { display: flex; align-items: center; gap: 5px; line-height: 1.3; }
  .contact-row svg { width: 11px; height: 11px; fill: var(--white); flex: none; }
  .board-brand {
    position: absolute;
    left: 0; right: 0; top: 962px;
    display: flex; flex-direction: column; align-items: center;
    color: var(--navy);
    font-weight: 600;
  }
  .board-brand .brand__mark { width: 34px; height: 34px; margin-bottom: 12px; }
  .board-brand .brand__name { font-size: 70px; }
  .board-brand .brand__sub { font-size: 17px; letter-spacing: 8px; }
</style>
</head>
<body>
  <div class="board-frame"></div>
  <h1 class="board-title">ENVELOPE SACO</h1>

  <section class="envelope envelope--front" aria-label="Frente do envelope">
    <div class="brand">
      <span class="brand__mark"></span>
      <span class="brand__name">VANTA</span>
      <span class="brand__sub">ENGENHARIA</span>
    </div>
    <div class="envelope__stripe"></div>
  </section>

  <section class="envelope envelope--back" aria-label="Verso do envelope">
    <svg class="envelope__flap" width="440" height="86" viewBox="0 0 440 86">
      <path d="M0 0 H440 V40 Q440 52 428 56 L380 84 H60 L12 56 Q0 52 0 40 Z" fill="var(--gold)"/>
    </svg>
    <div class="brand">
      <span class="brand__mark"></span>
      <span class="brand__name">VANTA</span>
      <span class="brand__sub">ENGENHARIA</span>
    </div>
    <div class="contact-row">
      <span class="contact-row__item">
        <svg viewBox="0 0 24 24"><path d="M6.6 10.8a15 15 0 0 0 6.6 6.6l2.2-2.2a1 1 0 0 1 1-.25 11.4 11.4 0 0 0 3.6.6 1 1 0 0 1 1 1V20a1 1 0 0 1-1 1A17 17 0 0 1 3 4a1 1 0 0 1 1-1h3.5a1 1 0 0 1 1 1c0 1.25.2 2.45.6 3.6a1 1 0 0 1-.25 1z"/></svg>
        (19) 4000-1234
      </span>
      <span class="contact-row__item">
        <svg viewBox="0 0 24 24"><path d="M2 5h20v14H2z M4 7v.4l8 5 8-5V7l-8 5z" fill-rule="evenodd"/></svg>
        contato@vantaeng.com.br
      </span>
      <span class="contact-row__item">
        <svg viewBox="0 0 24 24"><path d="M12 2a7 7 0 0 0-7 7c0 5 7 13 7 13s7-8 7-13a7 7 0 0 0-7-7zm0 9.5A2.5 2.5 0 1 1 12 6.5a2.5 2.5 0 0 1 0 5z"/></svg>
        <span>R. Aurora Lima, 210<br>Campinas - SP</span>
      </span>
    </div>
    <div class="envelope__stripe"></div>
  </section>

  <div class="board-brand">
    <span class="brand__mark"></span>
    <span class="brand__name">VANTA</span>
    <span class="brand__sub">ENGENHARIA</span>
  </div>
</body>
</html>
```